Gold Harbor Concierge

I need a website developed for our travel concierge service. I'm looking to be able to collect information and have the information collected directed to a inbox. I would also like to me able to manage the updates to the website myself. I also would like a mobile version of the website to be included. Our services include assistance with Bachelor Parties, Bachelorette Parties and Medical Tourism. We provide custom packages that include Airport Transportation, Lodging, Bilingual guides and any other special needs identified by our clients.
Industry/Entity Type
Travel
Coding
Coded - Design and coding required
Number of Pages Required
4 page
Look and feel

```html
<!DOCTYPE html>
<html lang="en">
<head>
<meta charset="utf-8">
<title>Gold Harbor Concierge</title>
<link href="https://fonts.googleapis.com/css2?family=Marcellus&family=Crimson+Text&family=Roboto:wght@700&display=swap" rel="stylesheet">
<style>
:root{
  --black:#000;
  --orange:#f39216;
  --white:#fff;
  --text-light:#e9e9e9;
  --text-grey:#6a6a6a;
  --pink-a:#d77ccb;
  --pink-b:#b35aa9;
  --beige-a:#e6d8c6;
  --beige-b:#d8c6ae;
  --rule:#3a3a3a;
}
*{margin:0;padding:0;box-sizing:border-box}
html,body{width:1200px;height:3934px;overflow:hidden;background:var(--black)}
body{position:relative;font-family:"Crimson Text",serif;color:var(--text-light)}
.abs{position:absolute}
.heading{font-family:"Marcellus",serif;color:var(--orange);letter-spacing:3px;text-align:center;font-weight:400;white-space:nowrap}
.rule-short{position:absolute;height:3px;background:var(--orange);width:62px;left:569px}
.lead{position:absolute;left:230px;width:740px;text-align:center;font-size:16px;line-height:25px;color:var(--text-light)}
.photo{position:absolute}
.btn{position:absolute;font-family:"Marcellus",serif;letter-spacing:2px;text-align:center;font-size:17px;white-space:nowrap}
.btn-dark{background:var(--black);color:var(--orange)}
.btn-orange{background:var(--orange);color:var(--black)}

/* header */
.top-label{font-family:"Marcellus",serif;font-size:14px;letter-spacing:2px;color:var(--white);text-align:center}
.top-contact{font-family:"Roboto",sans-serif;font-weight:700;font-size:20px;letter-spacing:2px;color:var(--orange);text-align:center;white-space:nowrap}
.brand{font-family:"Marcellus",serif;color:var(--orange);text-align:center;font-size:44px;line-height:46px;white-space:nowrap}
.brand small{display:block;font-size:13px;letter-spacing:8px;line-height:20px}
.nav{position:absolute;z-index:5;left:111px;top:186px;width:978px;height:52px;background:var(--white);display:flex;justify-content:space-around;align-items:center;padding:0 40px}
.nav a{font-family:"Marcellus",serif;color:#111;text-decoration:none;font-size:17px;line-height:52px}

/* services */
.card-label{position:absolute;width:312px;text-align:center;font-size:18px;color:var(--white);font-family:"Marcellus",serif}
.lodging{position:absolute;left:443px;top:1542px;width:313px;height:261px;background:var(--orange);color:#222;text-align:center;padding:24px 18px}
.lodging h3{font-family:"Marcellus",serif;font-weight:400;font-size:23px;margin-bottom:8px;color:#111}
.lodging p{font-size:14px;line-height:21px}

/* events */
.event{position:absolute;top:2153px;width:474px;height:376px;border:2px solid var(--orange)}
.event .date{position:absolute;right:12px;top:12px;width:117px;height:70px;background:var(--black);color:var(--orange);display:flex;align-items:center;justify-content:center;gap:6px;font-family:"Marcellus",serif}
.event .date span{font-size:17px;line-height:19px}
.event .date b{font-weight:400;font-size:50px}
.event .caption{position:absolute;left:16px;top:304px;font-family:"Marcellus",serif;color:var(--orange);font-size:17px;line-height:24px;white-space:nowrap}

/* newsletter */
.news{position:absolute;left:111px;top:2623px;width:978px;height:199px;background:linear-gradient(90deg,var(--beige-a),var(--beige-b));border-bottom:5px solid var(--orange)}

/* about */
.about-box{position:absolute;left:547px;top:2953px;width:542px;height:368px;background:var(--white);padding:26px 27px}

/* footer */
.f-title{position:absolute;font-size:19px;color:var(--orange)}
.f-bar{position:absolute;height:3px;width:58px;background:var(--orange)}
.f-text{position:absolute;font-size:14px;line-height:21px;color:var(--white)}
.f-key{position:absolute;font-size:14px;color:var(--orange)}
.f-vline{position:absolute;width:1px;background:var(--rule);top:3537px;height:274px}
</style>
</head>
<body>

<header>
  <div class="abs top-label" style="left:111px;width:240px;top:58px">GET A QUOTE</div>
  <div class="abs top-contact" style="left:76px;width:310px;top:82px;font-size:19px">HELLO@GOLDHARBOR.COM</div>
  <div class="abs" style="left:176px;top:124px;width:46px;height:44px;background:#2d4d9c"></div>
  <div class="abs" style="left:228px;top:124px;width:46px;height:44px;background:#c13584"></div>

  <div class="abs brand" style="left:440px;width:320px;top:52px">Gold Harbor<small>CONCIERGE</small></div>

  <div class="abs top-label" style="left:870px;width:280px;top:62px">CALL TO BOOKING</div>
  <div class="abs top-contact" style="left:870px;width:280px;top:84px">415-730-2284</div>
  <div class="abs" style="left:976px;top:122px;width:68px;height:49px;background:var(--white);border-radius:4px"></div>

  <nav class="nav">
    <a href="#">HOME</a><a href="#">ABOUT US</a><a href="#">OUR SERVICES</a><a href="#">UPDATES</a><a href="#">CONTACT US</a>
  </nav>
</header>

<section>
  <div class="photo" role="img" aria-label="Group of men celebrating at a party with confetti and drinks" style="left:0;top:213px;width:1200px;height:573px;background:linear-gradient(110deg,#3a1a22 0%,#7a3a44 25%,#3b3b44 55%,#707a80 80%,#2a2e33 100%)"></div>
  <div class="abs" style="left:0;top:786px;width:1200px;height:97px;background:var(--orange)"></div>
  <div class="abs" style="left:111px;top:690px;width:978px;height:200px;background:linear-gradient(100deg,var(--pink-a),var(--pink-b));border-bottom:6px solid var(--orange)"></div>
  <div class="photo" role="img" aria-label="Champagne bottle popping its cork" style="left:111px;top:700px;width:170px;height:184px;background:linear-gradient(135deg,rgba(255,255,255,0.35),rgba(60,50,30,0.6))"></div>
  <h1 class="abs heading" style="left:300px;width:600px;top:702px;font-size:40px;color:var(--white);letter-spacing:4px">BACHELOR PARTIES</h1>
  <p class="abs" style="left:285px;width:630px;top:757px;text-align:center;font-size:18px;line-height:25px;color:var(--white)">Lorem Ipsum is simply dummy text of the printing and typesetting industry. Lorem Ipsum has been the industry's standard dummy text ever since the 1500s,</p>
  <div class="btn btn-dark" style="left:470px;top:824px;width:261px;height:39px;line-height:39px">BOOK YOUR PARTIES</div>
</section>

<section>
  <h2 class="abs heading" style="left:0;width:1200px;top:978px;font-size:40px">OUR SERVICES</h2>
  <div class="rule-short" style="top:1043px"></div>
  <p class="lead" style="top:1062px">Lorem Ipsum is simply dummy text of the printing and typesetting industry. Lorem Ipsum has been the industry's standard dummy text ever since the 1500s, when an unknown printer took a galley of type and scrambled it to make a type specimen book. It has survived not only five centuries,</p>

  <div class="photo" role="img" aria-label="Group of young men laughing together" style="left:111px;top:1174px;width:312px;height:261px;background:linear-gradient(135deg,#6b4a3a,#a2876e,#4c3b33)"></div>
  <div class="photo" role="img" aria-label="Women toasting at a candle-lit dinner table" style="left:443px;top:1174px;width:313px;height:261px;background:linear-gradient(135deg,#2b2620,#5a4a35,#1e1a16)"></div>
  <div class="photo" role="img" aria-label="Toy airplane with a stethoscope on a passport" style="left:776px;top:1174px;width:313px;height:261px;background:linear-gradient(135deg,#7c7e86,#a9a3a0,#5a3a30)"></div>
  <div class="card-label" style="left:111px;top:1451px">BACHELOR PARTIES</div>
  <div class="card-label" style="left:443px;top:1451px">BACHELORETTE PARTIES</div>
  <div class="card-label" style="left:776px;top:1451px">MEDICAL TOURISM</div>

  <div class="photo" role="img" aria-label="Masked traveller waiting at an airport with luggage" style="left:111px;top:1542px;width:312px;height:261px;background:linear-gradient(135deg,#3d5a8c,#6c84b8,#c58a2c)"></div>
  <div class="lodging">
    <h3>LODGING</h3>
    <p>Lorem Ipsum is simply dummy text of the printing and typesetting industry. Lorem Ipsum has been the industry's standard dummy text ever since the 1500s, when an unknown printer took a galley of type and scrambled it to make a type specimen book. It has survived not only five centuries, but also the leap into electronic typesetting, remaining</p>
  </div>
  <div class="btn btn-orange" style="left:443px;top:1817px;width:313px;height:37px;line-height:37px">BOOK NOW</div>
  <div class="photo" role="img" aria-label="Traveller in a sun hat reading a map by a turquoise door" style="left:776px;top:1542px;width:313px;height:261px;background:linear-gradient(135deg,#5fd6d2,#8ee3dc,#3ab9b6)"></div>
  <div class="card-label" style="left:111px;top:1819px">LOREM IPSUM</div>
  <div class="card-label" style="left:776px;top:1819px">NEQUE PORRO QUISQUAM</div>
</section>

<section>
  <h2 class="abs heading" style="left:0;width:1200px;top:1988px;font-size:40px">UPCOMMING PARTIES</h2>
  <div class="rule-short" style="top:2053px"></div>
  <p class="lead" style="top:2071px">Lorem Ipsum is simply dummy text of the printing and typesetting industry. Lorem Ipsum has been the industry's standard dummy text ever since the 1500s, when an unknown printer</p>

  <div class="event" style="left:111px">
    <div class="photo" role="img" aria-label="Friends clinking beer bottles at a bar" style="left:0;top:0;width:470px;height:300px;background:linear-gradient(180deg,#3d6a8c 0%,#5a6670 50%,#000 100%)"></div>
    <div class="date"><span>DEC<br>2021</span><b>12</b></div>
    <div class="caption">NEQUE PORRO<br>QUISQUAM EST QUI DOLOREM</div>
    <div class="btn btn-orange" style="left:302px;top:306px;width:151px;height:39px;line-height:39px">BOOK NOW</div>
  </div>
  <div class="event" style="left:615px">
    <div class="photo" role="img" aria-label="Women celebrating a bachelorette party with drinks" style="left:0;top:0;width:470px;height:300px;background:linear-gradient(180deg,#4a2a40 0%,#8a4a5e 45%,#000 100%)"></div>
    <div class="date"><span>DEC<br>2021</span><b>13</b></div>
    <div class="caption">NEQUE PORRO<br>QUISQUAM EST QUI DOLOREM</div>
    <div class="btn btn-orange" style="left:302px;top:306px;width:151px;height:39px;line-height:39px">BOOK NOW</div>
  </div>
</section>

<section>
  <div class="news">
    <div class="photo" role="img" aria-label="Gold confetti and a champagne bottle" style="right:0;top:0;width:200px;height:194px;background:linear-gradient(110deg,rgba(230,216,198,0),#c9a76a 70%,#a88446)"></div>
    <h2 class="abs heading" style="left:0;width:978px;top:38px;font-size:42px;color:#111;letter-spacing:4px">JOIN OUR NEWSLETTER</h2>
    <div class="abs" style="left:185px;top:107px;width:452px;height:35px;background:var(--black);color:var(--orange);font-family:'Marcellus',serif;letter-spacing:2px;font-size:17px;line-height:35px;padding-left:25px">EMAIL ADDRESS</div>
    <div class="btn btn-dark" style="left:643px;top:107px;width:148px;height:35px;line-height:35px">SUBSCRIBE</div>
  </div>
</section>

<section>
  <div class="photo" role="img" aria-label="Open hand under five glowing rating stars" style="left:111px;top:2906px;width:585px;height:462px;border:2px solid var(--orange);background:radial-gradient(circle at 45% 45%,#4f7a92,#1d3a4e 70%,#0e1f2c)"></div>
  <div class="about-box">
    <h2 class="heading" style="text-align:left;font-size:33px;letter-spacing:3px;line-height:44px">GOLD HARBOR CONCIERGE</h2>
    <p style="margin-top:22px;color:var(--text-grey);font-size:16px;line-height:25px">Lorem Ipsum is simply dummy text of the printing and typesetting industry. Lorem Ipsum has been the industry's standard dummy text ever since the 1500s, when an unknown printer took a galley of type and scrambled it to make a type specimen book. It has survived not only five centuries, but also the leap into electronic typesetting, remaining essentially unchanged. It was popularised in the 1960s with the release of Letraset sheets containing Lorem Ipsum passages, and</p>
    <div class="btn btn-orange" style="left:27px;top:298px;width:151px;height:37px;line-height:37px">BOOK NOW</div>
  </div>
</section>

<footer>
  <div class="abs" style="left:111px;top:3494px;width:978px;height:1px;background:var(--rule)"></div>
  <div class="f-vline" style="left:440px"></div>
  <div class="f-vline" style="left:785px"></div>

  <div class="f-title" style="left:114px;top:3537px">Help &amp; Support</div>
  <div class="f-bar" style="left:114px;top:3571px"></div>
  <div class="f-key" style="left:115px;top:3598px">Gold Harbor Concierge</div>
  <div class="f-text" style="left:115px;top:3628px">712 Lantern Row,&nbsp; CEDAR BAY,<br>Oregon, 97140.</div>
  <div class="f-key" style="left:115px;top:3692px">Phone:</div>
  <div class="f-text" style="left:115px;top:3714px">415-730-2284</div>
  <div class="f-key" style="left:115px;top:3758px">Email:</div>
  <div class="f-text" style="left:115px;top:3780px">hello@goldharbor.com</div>

  <div class="f-title" style="left:566px;top:3536px">Sitemap</div>
  <div class="f-bar" style="left:566px;top:3570px"></div>
  <div class="f-text" style="left:568px;top:3601px;line-height:30px">Home<br>About US<br>Our Services<br>Updates<br>Contact Us</div>

  <div class="abs brand" style="left:860px;width:270px;top:3610px;font-size:40px;line-height:42px">Gold Harbor<small>CONCIERGE</small></div>

  <div class="abs" style="left:111px;top:3847px;width:978px;height:1px;background:var(--rule)"></div>
  <div class="abs" style="left:0;width:1200px;top:3878px;text-align:center;font-size:14px;color:var(--white)">Gold Harbor Concierge .All copyrights reserved © 2021.</div>
</footer>

</body>
</html>
```